Business Card Design Project

Business card design for an IT Service company. A logo has already been created in a different contest and has been attached to this project. Ideally we're looking for a double sided business card that matches the look and feel of our newly created logo.

We're open to creativity if you feel a tag line is needed such as "IT Services and Application Development". We're open to really and look and feel - even single sided business cards if you feel you have something that's a great idea.

Last thought here - I'm not sure how it'll look but maybe a two tone card? One side dark blue and the other side white? Don't limit the design submissions to this tho - just curious if it would look good

Nothing too busy please - simple... Thank you and happy designing!

Target Market(s)

Businesses that require IT Services and support for hosted services, technical consultation, web design.

Industry/Entity Type

Business

Font styles to use
Sans Serif

Requirements
Must have
• Use the colors provided in the logo (see attachment) or additional colors that compliment
Must have the following contact info (not necessarily in this order):
- Alan Fisk
- Founding Partner
- afisk@quillbarrow.example
- 555-382-1946
- www.quillbarrow.example

```html
<!DOCTYPE html>
<html lang="en">
<head>
<meta charset="utf-8">
<title>Quillbarrow – Business Card</title>
<link rel="stylesheet" href="https://fonts.googleapis.com/css2?family=Source+Sans+3:wght@400;600;700&display=swap">
<style>
  :root {
    --navy: #0d1b5e;
    --sky: #00a3ff;
    --ink: #111111;
    --rule-grey: #d9d9d9;
    --texture-grey: #ececec;
    --paper: #ffffff;
  }
  * { margin: 0; padding: 0; box-sizing: border-box; }
  html, body { width: 1200px; height: 720px; overflow: hidden; background: var(--paper); }
  body { font-family: "Source Sans 3", "Myriad Pro", Arial, sans-serif; color: var(--ink); }

  .card { position: relative; width: 1200px; height: 720px; background: var(--paper); overflow: hidden; }

  .top-texture { position: absolute; left: 0; top: 0; width: 1200px; height: 139px; background: var(--texture-grey); }

  .brand { position: absolute; left: 116px; top: 224px; }
  .brand-name { display: block; font-size: 76px; font-weight: 700; color: var(--navy); line-height: 1; letter-spacing: -0.5px; white-space: nowrap; }
  .tagline { position: absolute; left: 127px; top: 292px; font-size: 24px; line-height: 1; font-weight: 400; color: var(--ink); white-space: nowrap; }

  .person { position: absolute; right: 114px; top: 175px; text-align: right; white-space: nowrap; }
  .person-name { font-size: 44px; line-height: 1; letter-spacing: -0.5px; text-transform: uppercase; font-weight: 400; }
  .person-name .first { color: var(--sky); font-weight: 700; }
  .person-name .last { color: var(--ink); font-weight: 400; }
  .person-role { font-size: 27px; line-height: 1; font-weight: 400; margin-top: 1px; }

  .rule-grey { position: absolute; left: 0; top: 350px; width: 823px; height: 10px; background: var(--rule-grey); }
  .rule-blue { position: absolute; left: 834px; top: 350px; width: 366px; height: 10px; background: var(--sky); }

  .contacts { position: absolute; left: 110px; top: 378px; list-style: none; }
  .contact { position: absolute; left: 0; display: flex; align-items: center; white-space: nowrap; font-size: 25px; line-height: 32px; height: 32px; }
  .contact svg { width: 30px; height: 30px; margin-right: 20px; fill: var(--ink); flex: none; }
  .contact-address { top: 0; }
  .contact-phone { top: 50px; }
  .contact-email { top: 107px; }
  .contact-web { top: 151px; }

  .bottom-band { position: absolute; left: 0; top: 581px; width: 1200px; height: 139px; background: var(--sky); }
</style>
</head>
<body>
<main class="card">
  <div class="top-texture" role="img" aria-label="Fine diagonal grey line texture"></div>

  <div class="brand">
    <span class="brand-name">Quillbarrow</span>
  </div>
  <p class="tagline">IT Services and Application Development</p>

  <div class="person">
    <h1 class="person-name"><span class="first">Alan</span> <span class="last">Fisk</span></h1>
    <p class="person-role">Founding Partner</p>
  </div>

  <div class="rule-grey"></div>
  <div class="rule-blue"></div>

  <ul class="contacts">
    <li class="contact contact-address">
      <svg viewBox="0 0 24 24" aria-hidden="true"><path d="M12 1C7.6 1 4.5 4.2 4.5 8.4 4.5 13.5 12 23 12 23s7.5-9.5 7.5-14.6C19.5 4.2 16.4 1 12 1zm0 10.2a2.8 2.8 0 1 1 0-5.6 2.8 2.8 0 0 1 0 5.6z"/></svg>
      418 Harlow Street, Brookfield 60917
    </li>
    <li class="contact contact-phone">
      <svg viewBox="0 0 24 24" aria-hidden="true"><path d="M7.5 1h9A1.5 1.5 0 0 1 18 2.5v19a1.5 1.5 0 0 1-1.5 1.5h-9A1.5 1.5 0 0 1 6 21.5v-19A1.5 1.5 0 0 1 7.5 1zm.3 3v14.5h8.4V4zM12 19.6a1.1 1.1 0 1 0 0 2.2 1.1 1.1 0 0 0 0-2.2z"/></svg>
      555-382-1946
    </li>
    <li class="contact contact-email">
      <svg viewBox="0 0 24 24" aria-hidden="true"><path d="M1.5 5h21v14h-21zm2 1.6L12 13l8.5-6.4zm-.4 1.6v9.2l5.6-5zm17.8 0-5.6 4.2 5.6 5zM10 12.4l-5.8 5h15.6l-5.8-5-2 1.5z"/></svg>
      afisk@quillbarrow.example
    </li>
    <li class="contact contact-web">
      <svg viewBox="0 0 24 24" aria-hidden="true"><path d="M10.6 13.4a1 1 0 0 1 0-1.4l4.2-4.2a1 1 0 1 1 1.4 1.4L12 13.4a1 1 0 0 1-1.4 0zm-1.3 5.9a4 4 0 0 1-5.7-5.7l3-3 1.4 1.4-3 3a2 2 0 0 0 2.9 2.9l3-3 1.4 1.4zm8.1-5.9-1.4-1.4 3-3a2 2 0 0 0-2.9-2.9l-3 3-1.4-1.4 3-3a4 4 0 0 1 5.7 5.7z"/></svg>
      www.quillbarrow.example
    </li>
  </ul>

  <div class="bottom-band"></div>
</main>
</body>
</html>
```